Fitness Company Valentine's Day Special Flyer

We need an 8x10 flyer designed for our Valentine's Day Special Promo offer to the public. We've included the flyer's text and details - please include all information in the word document attached. DO NOT use this as a design template just the information. We expect something awesome!!!
- The flyer MUST be 8x10 in PSD format (CS3 Compatible) INCLUDING ALL Layers and Fonts
- Please include fitness pictures
- Include our Logo (attached)
- ***Please use the color schemes used in our logo to help with the design!!!!
Industry/Entity Type
Fitness
Look and feel
Each slider illustrates characteristics of the customer's brand and the style your logo design should communicate.

```html
<!DOCTYPE html>
<html lang="en">
<head>
<meta charset="utf-8">
<title>Valentine's Day 2-for-1 Special Flyer</title>
<link href="https://fonts.googleapis.com/css2?family=Bebas+Neue&family=Yellowtail&family=Open+Sans:wght@400;600;700&display=swap" rel="stylesheet">
<style>
  :root {
    --bg: #d9c2e6;
    --purple-deep: #5e1f86;
    --purple: #7b2fa8;
    --purple-mid: #9a4cc4;
    --pink: #d23fd6;
    --pink-soft: #e27ce4;
    --lilac: #c99ee0;
    --white: #ffffff;
    --grey-text: #5a5a5a;
    --skin-a: #c8a590;
    --skin-b: #8f6f63;
  }
  * { box-sizing: border-box; margin: 0; padding: 0; }
  html, body { width: 1200px; height: 1000px; overflow: hidden; }
  body { background: var(--bg); font-family: "Open Sans", Arial, sans-serif; position: relative; }

  .flyer {
    position: absolute; left: 240px; top: 50px;
    width: 720px; height: 900px;
    background: var(--white); overflow: hidden;
    box-shadow: 0 10px 30px rgba(60, 20, 90, .25);
  }
  .flyer__photo {
    position: absolute; left: 0; top: 0; width: 720px; height: 560px;
    background:
      radial-gradient(ellipse at 30% 35%, var(--skin-a), transparent 55%),
      radial-gradient(ellipse at 72% 70%, var(--skin-a), transparent 55%),
      linear-gradient(135deg, var(--skin-b), #b48d7a 45%, var(--purple-mid) 100%);
  }
  .flyer__swoosh { position: absolute; left: 0; top: 0; width: 720px; height: 900px; }

  .headline { position: absolute; right: 30px; top: 26px; width: 440px; text-align: center; }
  .headline__script {
    font-family: "Yellowtail", cursive; font-weight: 400; font-size: 96px; line-height: .95;
    color: var(--pink); -webkit-text-stroke: 3px var(--white);
    paint-order: stroke fill; text-shadow: 0 3px 6px rgba(0,0,0,.25);
  }
  .headline__sub {
    font-family: "Bebas Neue", sans-serif; font-size: 34px; letter-spacing: 1px;
    color: var(--purple); margin-top: 4px;
  }

  .tagline {
    position: absolute; left: 36px; top: 456px; width: 600px;
    font-family: "Bebas Neue", sans-serif; font-size: 30px; line-height: 1.05;
    color: var(--white); letter-spacing: .5px;
  }
  .tagline__accent { color: var(--pink-soft); }

  .offer { position: absolute; left: 36px; top: 556px; width: 440px; color: var(--grey-text); font-size: 14.5px; line-height: 1.35; }
  .offer__list { list-style: none; margin-top: 8px; font-weight: 700; font-size: 13.5px; line-height: 1.4; }
  .offer__list li::before { content: "•"; color: var(--purple); margin-right: 6px; }
  .offer__love { margin-top: 12px; font-size: 22px; font-weight: 600; color: var(--pink); line-height: 1.3; }
  .offer__benefits { font-size: 21px; font-weight: 600; color: var(--purple); line-height: 1.3; }

  .price-heart { position: absolute; left: 495px; top: 575px; width: 210px; height: 190px; }
  .price-heart__text {
    position: absolute; left: 0; top: 42px; width: 210px; text-align: center;
    font-family: "Bebas Neue", sans-serif; color: var(--white); line-height: 1;
    transform: rotate(-8deg);
  }
  .price-heart__deal { font-size: 30px; }
  .price-heart__amount { font-size: 44px; }

  .contact { position: absolute; left: 36px; top: 806px; width: 330px; color: var(--white); font-size: 11px; line-height: 1.45; }
  .contact__hl { color: var(--pink-soft); font-weight: 700; }

  .brand {
    position: absolute; right: 30px; bottom: 22px; width: 300px; height: 62px;
    background: var(--white); border: 3px solid var(--lilac);
    display: flex; align-items: center; justify-content: center; gap: 10px; padding: 0 14px;
  }
  .brand__mark { width: 14px; height: 14px; background: var(--purple); flex: none; }
  .brand__name { font-family: "Bebas Neue", sans-serif; font-size: 27px; line-height: 1; color: var(--purple); letter-spacing: 1px; white-space: nowrap; }
</style>
</head>
<body>
  <main class="flyer">
    <div class="flyer__photo" role="img" aria-label="Photo of a fit couple's torsos, each making a heart shape with their hands over the stomach"></div>

    <svg class="flyer__swoosh" viewBox="0 0 720 900" aria-hidden="true">
      <path d="M0 430 C180 410 420 420 720 520 L720 900 L0 900 Z" fill="var(--purple)"/>
      <path d="M0 540 C260 530 420 560 500 640 C560 700 600 770 720 780 L720 900 L0 900 Z" fill="var(--purple-mid)" transform="translate(0 -10)"/>
      <path d="M0 540 C260 530 420 560 500 640 C560 700 600 770 720 780 L720 900 L0 900 Z" fill="var(--white)"/>
      <path d="M0 792 C200 772 420 802 720 782 L720 900 L0 900 Z" fill="var(--purple-deep)"/>
      <path d="M0 782 C220 762 420 792 720 772 L720 784 C420 804 220 774 0 796 Z" fill="var(--pink)"/>
      <path d="M600 770 l20 -18 a14 14 0 0 1 20 20 l-20 18 l-20 -18 a14 14 0 0 1 20 -20 Z" fill="var(--lilac)" opacity=".7"/>
    </svg>

    <header class="headline">
      <h1 class="headline__script">Valentine's Day</h1>
      <p class="headline__sub">2-for-1 Special</p>
    </header>

    <p class="tagline">Couples that train together stay together<br>this <span class="tagline__accent">Valentine's Day</span> train together!</p>

    <section class="offer">
      <p>The perfect gift for You and Your Valentine.<br>Included In Your 30 Day Jumpstart:</p>
      <ul class="offer__list">
        <li>Success Start Consultation</li>
        <li>12 Group Personal Training Sessions</li>
        <li>Success Manual with Bonus Nutrition Guide</li>
        <li>Unlimited Coaching Support via Private Members Online Group</li>
      </ul>
      <p class="offer__love">Love Your Body This Valentine's Day</p>
      <p class="offer__benefits">Move Better | Look Better | Feel Better</p>
    </section>

    <div class="price-heart">
      <svg viewBox="0 0 210 190" width="210" height="190" aria-hidden="true">
        <path d="M105 185 L18 98 A50 50 0 0 1 105 30 A50 50 0 0 1 192 98 Z" fill="var(--pink)"/>
      </svg>
      <div class="price-heart__text">
        <p class="price-heart__deal">2-for-1 Special</p>
        <p class="price-heart__amount">Only $99</p>
      </div>
    </div>

    <footer class="contact">
      <p>Call Us Now at <span class="contact__hl">555-0142</span> to Reserve This Offer!</p>
      <p>Expires February 14th | Only 20 Spots Available</p>
      <p>PulseForge Bootcamps</p>
      <p>1200 Main St Unit 14 Fairview CO 80999</p>
      <p>www.pulseforgefit.com</p>
    </footer>

    <div class="brand">
      <span class="brand__mark"></span>
      <span class="brand__name">PulseForge Bootcamps</span>
    </div>
  </main>
</body>
</html>
```